Templates for Construction Company

We are looking to have templates prepared for all aspects of our letter sending. Using our brand design. with similar layouts that look the same.

Letterheads design & Email signatures

We use letter heads for - quotes, contract correspondence, variations, formal letters, invitations

Target Market(s)

Clients documents sent in emails

Industry/Entity Type

Construction

Font styles to use
Serif
Sans Serif

Colors
0054AA
0677BA
7BADD7
CADEEF
E8F1F8

Requirements
Must have
• Easy to read, water marks on page
Nice to have
• Different options for different letters

```html
<!DOCTYPE html>
<html lang="en">
<head>
<meta charset="utf-8">
<title>Forge Construction Group – Envelope Set</title>
<link href="https://fonts.googleapis.com/css2?family=Montserrat:wght@500;700&display=swap" rel="stylesheet">
<style>
  :root {
    --bg: #e9e9e9;
    --paper: #ffffff;
    --paper-edge: #dcdcdc;
    --brand-blue: #5580ae;
    --ink-grey: #5c5c5c;
    --tint-strong: #ededed;
    --tint-soft: rgba(237, 237, 237, 0);
    --flap-text: #ffffff;
  }
  * { margin: 0; padding: 0; box-sizing: border-box; }
  html, body {
    width: 1200px;
    height: 795px;
    overflow: hidden;
    background: var(--bg);
    font-family: "Montserrat", Arial, sans-serif;
  }
  .stationery {
    width: 1200px;
    height: 795px;
    display: flex;
    align-items: center;
    justify-content: center;
    gap: 56px;
  }
  .envelope {
    position: relative;
    width: 520px;
    height: 260px;
    background: var(--paper);
    border: 1px solid var(--paper-edge);
    box-shadow: 0 6px 14px rgba(0, 0, 0, 0.08);
    overflow: hidden;
  }
  .brand-lockup {
    display: flex;
    align-items: center;
    gap: 8px;
    white-space: nowrap;
  }
  .brand-square {
    width: 14px;
    height: 14px;
    flex: none;
    background: var(--brand-blue);
  }
  .brand-name {
    font-weight: 700;
    font-size: 17px;
    line-height: 1;
    color: var(--brand-blue);
  }

  /* Front */
  .sender {
    position: absolute;
    top: 32px;
    left: 34px;
  }
  .sender-address {
    margin-top: 9px;
    font-weight: 500;
    font-size: 10.5px;
    line-height: 1.5;
    color: var(--ink-grey);
  }
  .watermark-area {
    position: absolute;
    right: 0;
    bottom: 0;
    width: 230px;
    height: 150px;
    background: linear-gradient(315deg, var(--tint-strong) 0%, var(--tint-soft) 70%);
  }

  /* Back */
  .flap {
    position: absolute;
    top: 0;
    left: 0;
    width: 100%;
    height: 110px;
    background: var(--brand-blue);
    border-radius: 0 0 10px 10px;
    display: flex;
    align-items: center;
    justify-content: center;
  }
  .flap .brand-square { background: var(--flap-text); }
  .flap .brand-name { color: var(--flap-text); }
</style>
</head>
<body>
  <main class="stationery">
    <section class="envelope envelope-front" aria-label="Envelope front">
      <div class="sender">
        <div class="brand-lockup">
          <span class="brand-square"></span>
          <span class="brand-name">Forge Construction Group</span>
        </div>
        <p class="sender-address">48 Harbour Ridge Road,<br>Westfield, ON K2M 4T7</p>
      </div>
      <div class="watermark-area" role="img" aria-label="Faint brand watermark area"></div>
    </section>

    <section class="envelope envelope-back" aria-label="Envelope back">
      <div class="flap">
        <div class="brand-lockup">
          <span class="brand-square"></span>
          <span class="brand-name">Forge Construction Group</span>
        </div>
      </div>
    </section>
  </main>
</body>
</html>
```